Business card design for counselling and psychotherapy practice

I am seeking a business card for a new venture into private practice. I am based in Brisbane Qld Australia. I provide holistic counselling and psychotherapy to individuals and groups.
Some words that describe the underpinnings of this practice would include: being, becoming, awareness, wholeness, contact, safety, acceptance, relationship, gestalt, paradox, interconnected, nature, process.
I would like to see designs that include earth colours.
The overall design should communicate safety and a curiosity of being and becoming.
Target Market(s)
this design is marketed toward women, professionals, lesbian, transgender, mothers
Industry/Entity Type
Safety
Contact Information for Business Card
Fern & Hollow
Counselling and Psychotherapy
Noa Westby
ph: 0417392561
email: noa.fern&hollow@quillpost.example
www.fern&hollowcounselling&psychotherapy.example
Logo styles of interest
Abstract Logo
Look and feel
Each slider illustrates characteristics of the customer's brand and the style your logo design should communicate.

```html
<!DOCTYPE html>
<html lang="en">
<head>
<meta charset="utf-8">
<title>Fern &amp; Hollow Counselling and Psychotherapy – Business Card</title>
<link rel="stylesheet" href="https://fonts.googleapis.com/css2?family=Baloo+2:wght@700&family=Alfa+Slab+One&family=Lato:wght@400&display=swap">
<style>
  :root {
    --teal: #1a8e96;
    --teal-deep: #0f7d86;
    --teal-light: #2aa2a9;
    --white: #ffffff;
    --paper: #f7f9f9;
    --backdrop: #e4e6e7;
    --silver: #c9d3d5;
  }
  * { margin: 0; padding: 0; box-sizing: border-box; }
  html, body {
    width: 1200px; height: 960px; overflow: hidden;
    background: var(--backdrop);
  }
  .canvas {
    width: 1200px; height: 960px;
    display: flex; flex-direction: column; align-items: center; justify-content: center;
    gap: 56px;
  }
  .card {
    position: relative;
    width: 700px; height: 400px;
    overflow: hidden;
    box-shadow: 0 10px 28px rgba(0,0,0,0.18);
  }

  /* Front side */
  .card-front {
    background: linear-gradient(135deg, var(--teal-light) 0%, var(--teal) 55%, var(--teal-deep) 100%);
  }
  .card-front .title {
    position: absolute; left: 70px; top: 44px; width: 600px;
    font-family: "Baloo 2", "Trebuchet MS", sans-serif;
    font-weight: 700; font-size: 41px; line-height: 1.12;
    color: var(--white);
    text-shadow: 0 2px 3px rgba(0,0,0,0.25);
  }
  .card-front .swoosh {
    position: absolute; left: 80px; top: 140px; width: 580px; height: 40px;
  }
  .card-front .contact {
    position: absolute; left: 140px; top: 258px; width: 480px;
    font-family: "Lato", "Gill Sans", sans-serif; font-size: 16px; line-height: 1.4;
    color: var(--white); text-align: center;
  }
  .card-front .contact .phone { padding-left: 40px; }
  .card-front .footer-band {
    position: absolute; left: 0; bottom: 0; width: 100%; height: 70px;
  }

  /* Back side */
  .card-back { background: var(--paper); }
  .card-back .top-band {
    position: absolute; left: 0; top: 0; width: 100%; height: 28px;
    background: var(--teal);
    border-bottom: 3px solid var(--white);
  }
  .card-back .bottom-band {
    position: absolute; left: 0; bottom: 0; width: 100%; height: 72px;
    background: var(--teal);
  }
  .card-back .title {
    position: absolute; left: 40px; top: 70px; width: 630px;
    font-family: "Alfa Slab One", "Rockwell", serif;
    font-size: 34px; line-height: 1.02; letter-spacing: 0.5px;
    color: var(--teal);
  }
  .card-back .contact {
    position: absolute; right: 40px; top: 218px; width: 520px;
    font-family: "Lato", "Gill Sans", sans-serif; font-size: 15px; line-height: 1.4;
    letter-spacing: 1px; color: var(--teal); text-align: center;
  }
  .card-back .contact .web { letter-spacing: 0.6px; font-size: 14px; }
</style>
</head>
<body>
<main class="canvas">

  <section class="card card-front" aria-label="Business card front">
    <h1 class="title">Fern &amp; Hollow Counselling and Psychotherapy Noa Westby</h1>
    <svg class="swoosh" viewBox="0 0 580 40" aria-hidden="true">
      <defs>
        <linearGradient id="swooshFade" x1="0" x2="1">
          <stop offset="0" stop-color="#ffffff" stop-opacity="0"/>
          <stop offset="0.5" stop-color="#ffffff" stop-opacity="0.95"/>
          <stop offset="1" stop-color="#ffffff" stop-opacity="0"/>
        </linearGradient>
      </defs>
      <path d="M0 34 Q290 14 580 8" stroke="url(#swooshFade)" stroke-width="3" fill="none"/>
    </svg>
    <div class="contact">
      <p class="phone">Phone: 0417392561</p>
      <p class="email">Email: noa.fern&amp;hollow@quillpost.example</p>
      <p class="web">www.fern&amp;hollowcounselling&amp;psychotherapy.example</p>
    </div>
    <svg class="footer-band" viewBox="0 0 700 70" preserveAspectRatio="none" aria-hidden="true">
      <defs>
        <linearGradient id="bandFade" x1="0" x2="1">
          <stop offset="0" stop-color="#ffffff" stop-opacity="0"/>
          <stop offset="1" stop-color="#ffffff" stop-opacity="0.95"/>
        </linearGradient>
      </defs>
      <rect x="0" y="0" width="700" height="44" fill="url(#bandFade)"/>
      <rect x="0" y="44" width="700" height="4" fill="#c9d3d5"/>
      <rect x="0" y="48" width="700" height="22" fill="#0f7d86"/>
    </svg>
  </section>

  <section class="card card-back" aria-label="Business card back">
    <div class="top-band"></div>
    <h2 class="title">Fern &amp; Hollow Counselling and Psychotherapy Noa Westby</h2>
    <div class="contact">
      <p class="phone">Phone: 0417392561</p>
      <p class="email">Email: noa.fern&amp;hollow@quillpost.example</p>
      <p class="web">www.fern&amp;hollowcounselling&amp;psychotherapy.example</p>
    </div>
    <div class="bottom-band"></div>
  </section>

</main>
</body>
</html>
```